Ridgefold MMA - Ridgefold Way - 7-5-4

This will be for a wall logo. Probably printed on vinyl to adhere to the wall. This a rough draft concept of the project, but we're certainly open to other designs. Red, Black and White are the main colors we would like to use. The triangle motif is important, it denotes stability and base, which are important in jiu jistu.
The Ridgefold Way (7-5-4)
7 Virtues of a Warrior (Bushido)
R Rectitude
Doing what is right w/o regard for the consequences
C Courage
Inner strength to resist opposition. Courage not just to step on the mat but to make the right decisions
B Benevolence
Mindset to do good. Be kind and generous
P Politeness
Proper consideration and courtesy to others
L Loyalty
Faithfulness & Alliance. Not blind allegiance
H Honesty / Sincerity
Be a man of your word. Do what you say you will
Genuine Integrity in character & action
H Honor
Profound respect & ethical conduct
Make the right decisions to be worthy of respectability
5 Keys to Health
Nutrition - Eat sensibly
Exercise - Stay fit and ready
Rest - Recovery and Recharge
Hygiene - Stay Clean
Attitude - Assume positive intent
Look at life in a positive way
4 States of Mind (Spirit of Budo)
Shoshin - Beginners Mind
Be open to new ideas
Eager to Learn
Zanshin – Remaining Mind
Being Alert and Aware, but relaxed
Be Prepared
Mushin – No Mind (Clear Mind)
Be able to act in the moment without having to think
Fudoshin – Immovable Mind
Emotional Balance
Free from anger, fear, & doubt

```html
<!DOCTYPE html>
<html lang="en">
<head>
<meta charset="utf-8">
<title>The Ridgefold Way (7-5-4)</title>
<link rel="stylesheet" href="https://fonts.googleapis.com/css2?family=Ultra&family=Kanit:ital,wght@0,300;1,300&display=swap">
<style>
  :root {
    --red: #f20d0d;
    --black: #000000;
    --white: #ffffff;
    --display: "Ultra", serif;
    --body: "Kanit", sans-serif;
  }
  html, body {
    margin: 0;
    padding: 0;
    width: 1200px;
    height: 1200px;
    overflow: hidden;
    background: var(--white);
  }
  .poster {
    position: relative;
    width: 1200px;
    height: 1200px;
    background: var(--white);
    font-family: var(--body);
    color: var(--black);
  }
  .poster-shapes {
    position: absolute;
    inset: 0;
  }
  .block {
    position: absolute;
    transform: translateX(-50%);
    text-align: center;
    white-space: nowrap;
  }
  .title {
    margin: 0;
    font-family: var(--display);
    font-weight: 400;
    color: var(--red);
    font-size: 44px;
    line-height: 66px;
    left: 600px;
    top: 88px;
  }
  .virtues-heading {
    margin: 0;
    left: 600px;
    top: 290px;
    font-family: var(--display);
    font-weight: 400;
    font-size: 27px;
    line-height: 56px;
    color: var(--black);
  }
  .virtues-heading .count {
    color: var(--red);
    font-size: 58px;
    vertical-align: -6px;
    margin-right: 8px;
  }
  .virtues-heading .accent { color: var(--red); }

  .virtue h3 {
    margin: 0 0 6px;
    font-family: var(--display);
    font-weight: 400;
    color: var(--red);
    font-size: 22px;
    line-height: 28px;
  }
  .virtue p {
    margin: 0;
    font-size: 13.5px;
    line-height: 16px;
    font-weight: 300;
  }
  .virtue-rectitude   { left: 475px; top: 360px; }
  .virtue-courage     { left: 764px; top: 360px; }
  .virtue-benevolence { left: 600px; top: 473px; }
  .virtue-politeness  { left: 492px; top: 573px; }
  .virtue-loyalty     { left: 703px; top: 573px; }
  .virtue-honesty     { left: 600px; top: 680px; }
  .virtue-honor       { left: 600px; top: 795px; }

  .side-number {
    font-family: var(--display);
    color: var(--white);
    font-size: 58px;
    line-height: 60px;
  }
  .side-title {
    margin: 8px 0 0;
    font-family: var(--display);
    font-weight: 400;
    color: var(--red);
    font-size: 17px;
    line-height: 27px;
  }
  .side-list {
    position: absolute;
    transform: translateX(-50%);
    list-style: none;
    margin: 0;
    padding: 0;
    text-align: center;
    color: var(--white);
    white-space: nowrap;
  }
  .side-list li { margin: 0; }
  .side-list .item-name {
    display: block;
    font-family: var(--display);
    color: var(--red);
    font-size: 16px;
    line-height: 22px;
  }
  .side-list .item-text {
    display: block;
    font-size: 12px;
    line-height: 16px;
    font-weight: 300;
  }

  .health-head { left: 319px; top: 647px; color: var(--white); }
  .health-list { left: 319px; top: 779px; }
  .health-list li + li { margin-top: 18px; }

  .mind-head { left: 881px; top: 647px; }
  .mind-list { left: 881px; top: 810px; }
  .mind-list li + li { margin-top: 20px; }
  .mind-list .item-name { display: inline; }
  .mind-list .item-meaning {
    font-style: italic;
    font-weight: 300;
    font-size: 16px;
    line-height: 22px;
  }
  .mind-list .item-text { margin-top: 5px; }

  .brand-mark {
    left: 600px;
    top: 1069px;
    font-family: var(--display);
    color: var(--black);
    font-size: 16px;
    line-height: 26px;
  }
</style>
</head>
<body>
<main class="poster">
  <svg class="poster-shapes" width="1200" height="1200" viewBox="0 0 1200 1200" aria-hidden="true">
    <rect class="frame" x="40" y="40" width="1120" height="1120" fill="none" stroke="var(--black)" stroke-width="5"/>
    <path class="virtues-triangle" d="M 319 577 L 183 321 Q 162 277 210 271 L 990 271 Q 1038 277 1017 321 L 881 577"
          fill="none" stroke="var(--black)" stroke-width="8" stroke-linejoin="round"/>
    <polygon class="health-triangle" points="319,577 42,1086 605,1086" fill="var(--black)"/>
    <polygon class="mind-triangle" points="881,577 1158,1086 595,1086" fill="var(--black)"/>
    <rect class="base-band" x="42" y="1086" width="1116" height="72" fill="var(--red)"/>
    <circle class="brand-seal" cx="600" cy="1097" r="88" fill="var(--white)" stroke="var(--red)" stroke-width="9"/>
  </svg>

  <h1 class="block title">THE RIDGEFOLD WAY<br>(7-5-4)</h1>

  <h2 class="block virtues-heading"><span class="count">7</span>VIRTUES OF A WARRIOR <span class="accent">(BUSHIDO)</span></h2>

  <section class="block virtue virtue-rectitude">
    <h3>Rectitude</h3>
    <p>Doing what is right without<br>regard for the consequences</p>
  </section>
  <section class="block virtue virtue-courage">
    <h3>Courage</h3>
    <p>Inner strength to resist opposition.<br>Courage not just to step on the mat but<br>to make the right decisions</p>
  </section>
  <section class="block virtue virtue-benevolence">
    <h3>Benevolence</h3>
    <p>Have a mindset to do good.<br>Be kind and generous.</p>
  </section>
  <section class="block virtue virtue-politeness">
    <h3>Politeness</h3>
    <p>Have proper consideration<br>and courtesy for others.</p>
  </section>
  <section class="block virtue virtue-loyalty">
    <h3>Loyalty</h3>
    <p>Faithfulness &amp; Alliance.<br>Not blind allegiance.</p>
  </section>
  <section class="block virtue virtue-honesty">
    <h3>Honesty</h3>
    <p>Be a person of your word. Do what you<br>say you will. Have genuine integrity in<br>character and action.</p>
  </section>
  <section class="block virtue virtue-honor">
    <h3>Honor</h3>
    <p>Show profound<br>respect and ethical<br>conduct. Make the<br>right decisions to<br>be worth of<br>respectability.</p>
  </section>

  <div class="block health-head">
    <div class="side-number">5</div>
    <h2 class="side-title">KEYS<br>TO HEALTH</h2>
  </div>
  <ul class="side-list health-list">
    <li><span class="item-name">Nutrition</span><span class="item-text">Eat sensibly</span></li>
    <li><span class="item-name">Exercise</span><span class="item-text">Stay fit and ready</span></li>
    <li><span class="item-name">Rest</span><span class="item-text">Recover and Recharge</span></li>
    <li><span class="item-name">Hygiene</span><span class="item-text">Stay Clean</span></li>
    <li><span class="item-name">Attitude</span><span class="item-text">Assume positive intent. Look at life in a positive way.</span></li>
  </ul>

  <div class="block mind-head">
    <div class="side-number">4</div>
    <h2 class="side-title">STATES<br>OF MIND<br>(SPIRITS OF BUDO)</h2>
  </div>
  <ul class="side-list mind-list">
    <li><span class="item-name">Shoshin</span> <span class="item-meaning">- Beginners Mind</span><span class="item-text">Be open to new ideas. Be eager to learn.</span></li>
    <li><span class="item-name">Zanshin</span> <span class="item-meaning">– Remaining Mind</span><span class="item-text">Be alert and aware, but relaxed. Be prepared.</span></li>
    <li><span class="item-name">Mushin</span> <span class="item-meaning">– No Mind (Clear Mind)</span><span class="item-text">Be able to act in the moment without having to think</span></li>
    <li><span class="item-name">Fudoshin</span> <span class="item-meaning">– Immovable Mind</span><span class="item-text">Have emotional balance. Be free from anger, fear, and doubt.</span></li>
  </ul>

  <div class="block brand-mark">RIDGEFOLD<br>MMA</div>
</main>
</body>
</html>
```